Letterhead Design Project (logo provided)

We are a legal services provider company called VRN Legal based in the UK and would like some letterhead paper designed.

The design should use the attached logo, and should use the colors feature in the logo (along with blacks and/or greys).

The background paper must be white - and A4 size.

The letterhead should be provided in both .pdf and .doc (or .odf) formats.

Target Market(s)

Customers and clients for legal services

Industry/Entity Type

Legal

Requirements
Must have
• The header must include the following information:

Business name - VRN Legal LLP
Office address - Larchmead Court, Wallingford, Oxfordshire OX10 4TL, United Kingdom
Telephone - +44 (0)1491 736480
Email - mail@ [domain given below]
Website: www.vrnlegal-example.com

The footer must include the following information:

Registered office address - 14 Alder Row, Brindlecote, Wallingford, Oxfordshire OX10 6QD, United Kingdom
Companies House registration number - OC718463
VAT registration number - GB 417386205

```html
<!DOCTYPE html>
<html lang="en">
<head>
<meta charset="utf-8">
<title>VRN Legal Letterhead</title>
<link rel="stylesheet" href="https://fonts.googleapis.com/css2?family=Source+Sans+3:wght@400;600;700&family=Great+Vibes&display=swap">
<style>
  :root {
    --backdrop: #ececec;
    --paper: #ffffff;
    --ink: #3a3a3a;
    --ink-soft: #555555;
    --brand-blue: #1f66c1;
    --brand-green: #2fb52f;
  }
  * { box-sizing: border-box; margin: 0; padding: 0; }
  html, body {
    width: 1200px; height: 795px; overflow: hidden;
    background: var(--backdrop);
    font-family: "Source Sans 3", "Helvetica Neue", Arial, sans-serif;
    color: var(--ink);
  }
  .letterhead {
    position: absolute; left: 331px; top: 17px;
    width: 538px; height: 761px;
    background: var(--paper);
    box-shadow: 0 2px 10px rgba(0,0,0,0.12);
  }
  .letterhead__header {
    position: absolute; right: 56px; top: 46px;
    text-align: right;
  }
  .brand {
    display: flex; align-items: center; justify-content: flex-end; gap: 8px;
    font-size: 34px; font-weight: 600; color: var(--brand-blue);
    letter-spacing: 1px; line-height: 1;
  }
  .brand__dot {
    width: 16px; height: 16px; border-radius: 50%;
    background: var(--brand-green);
  }
  .contact {
    margin-top: 8px; font-size: 7.5px; line-height: 1.45; color: var(--ink);
  }
  .contact__web { color: var(--brand-blue); }
  .letter {
    position: absolute; left: 60px; top: 178px; width: 400px;
    font-size: 8.6px; line-height: 1.5; color: var(--ink-soft);
  }
  .letter__salutation { font-weight: 700; color: var(--ink); margin-bottom: 12px; font-size: 9px; }
  .letter p { margin-bottom: 12px; }
  .signoff { margin-top: 30px; }
  .signoff__signature {
    font-family: "Great Vibes", cursive; font-size: 30px; color: var(--ink); line-height: 1;
  }
  .signoff__title { font-weight: 700; font-size: 9px; color: var(--ink); margin-top: 2px; }
  .letterhead__footer {
    position: absolute; right: 24px; bottom: 30px;
    text-align: right; font-size: 7px; line-height: 1.45; color: var(--ink);
  }
  .footer-bands { position: absolute; left: 0; right: 0; bottom: 0; }
  .footer-bands__green { height: 3px; background: var(--brand-green); }
  .footer-bands__gap { height: 2px; background: var(--paper); }
  .footer-bands__blue { height: 10px; background: var(--brand-blue); }
</style>
</head>
<body>
  <main class="letterhead">
    <header class="letterhead__header">
      <div class="brand"><span class="brand__dot"></span>VRN Legal</div>
      <div class="contact">
        T: +44 (0)1491 736480 E: mail@vrnlegal-example.com<br>
        VRN Legal LLP Larchmead Court, Wallingford, Oxfordshire OX10 4TL, United Kingdom<br>
        <span class="contact__web">www.vrnlegal-example.com</span>
      </div>
    </header>

    <section class="letter">
      <div class="letter__salutation">Lorem Ipsum,</div>
      <p>Cras mattis consectetur purus sit amet fermentum. Etiam porta sem malesuada magna mollis euismod. Integer posuere erat a ante venenatis dapibus posuere velit aliquet. Cras justo odio, dapibus ac facilisis in, egestas eget quam. Aenean eu leo quam. Pellentesque ornare sem lacinia quam venenatis vestibulum.</p>
      <p>Vivamus sagittis lacus vel augue laoreet rutrum faucibus dolor auctor. Donec sed odio dui. Etiam porta sem malesuada magna mollis euismod. Morbi leo risus, porta ac consectetur ac, vestibulum at eros. Nullam id dolor id nibh ultricies vehicula ut id elit.</p>
      <p>Donec id elit non mi porta gravida at eget metus. Fusce dapibus, tellus ac cursus commodo, tortor mauris condimentum nibh, ut fermentum massa justo sit amet risus. Cras justo odio, dapibus ac facilisis in, egestas eget quam. Cum sociis natoque penatibus et magnis dis parturient montes, nascetur ridiculus mus.</p>
      <p>Cum sociis natoque penatibus et magnis dis parturient montes, nascetur ridiculus mus. Curabitur blandit tempus porttitor. Aenean lacinia bibendum nulla sed consectetur. Lorem ipsum dolor sit amet, consectetur adipiscing elit.</p>
      <p>Cras justo odio, dapibus ac facilisis in, egestas eget quam. Morbi leo risus, porta ac consectetur ac, vestibulum at eros. Duis mollis, est non commodo luctus, nisi erat porttitor ligula, eget lacinia odio sem nec elit. Integer posuere erat a ante venenatis dapibus posuere velit aliquet. Vivamus sagittis lacus vel augue laoreet rutrum faucibus dolor auctor.</p>
      <div class="signoff">
        <div class="signoff__signature">Your Name</div>
        <div class="signoff__title">Company Director</div>
      </div>
    </section>

    <footer class="letterhead__footer">
      Registered office address: 14 Alder Row, Brindlecote, Wallingford, Oxfordshire OX10 6QD, United Kingdom<br>
      Companies House registration number: OC718463 | VAT registration number: GB 417386205
    </footer>
    <div class="footer-bands">
      <div class="footer-bands__green"></div>
      <div class="footer-bands__gap"></div>
      <div class="footer-bands__blue"></div>
    </div>
  </main>
</body>
</html>
```